COMMERCIAL OFFICE FOR SALE- Brochure, Miami, FL 33131

BROCHURE DESIGN BRIEF – COMMERCIAL OFFICE FOR SALE

I need a clean, modern brochure for a commercial office listing (FOR SALE, not lease). This will be used both digitally (email + PlotHarbor/attachments) and printed if needed.

Please follow a “Sample Flyer Copy” style layout — strong headline, clean sections, minimal clutter, and easy to scan. Use fints Seasons and Poppins interchangeably.

All property details, specs, and exact wording should be pulled directly from the MLS Listing file I provided. Do not guess or rewrite specs.

OVERALL LOOK + FEEL

Clean, high-end, professional (Brickell / financial district vibe)

Think: simple, sharp, not busy

Neutral palette (white, black, soft gray) + subtle accent color if needed

Prioritize readability over design gimmicks

Plenty of white space

FORMAT

1-page flyer (primary)

Also format so it can easily convert into a 2-page version if needed

PDF optimized for email + print

HEADER SECTION (TOP OF PAGE)

Large, strong headline:

Example: “Office Condo for Sale | Brickell” (adjust based on MLS info)

Subheadline (smaller):

Key positioning (corner unit, square footage, etc.)

Include 1 strong hero image (best photo of the unit)

PROPERTY OVERVIEW (RIGHT UNDER HEADER OR NEXT BLOCK)

Clean bullet section with icons if possible:

Include:

Total square footage

Layout highlights (conference room, offices, open workspace, etc.)

Kitchen / breakroom

Reception area

Storage / printer room

Floor or suite number

Any standout feature (corner unit, natural light, views, etc.)

Keep this tight and clean — no long paragraphs.

PRICING SECTION

Clearly state: FOR SALE

Price (from MLS)

Price per square foot

Make this visually stand out.

LOCATION SECTION

Short and clean:

Building name + address

1–2 lines max on location advantages (Brickell, access, etc.)

Optional small map if it fits cleanly

ADDITIONAL DETAILS (IF SPACE ALLOWS)

Building amenities (if relevant)

Parking info

Zoning / permitted uses (if applicable)

Only include what is confirmed in MLS.

IMAGES

3–5 total max

Keep it clean — do not overcrowd

Prioritize:

Main workspace

Conference room

Kitchen

Any standout feature

CONTACT SECTION (VERY IMPORTANT – EXACT FORMAT)

This must be clean and prominent.

Delia Moncrief
REALTOR®
Tallowbrook Keystead Partners QNV Realty

Phone: [your number]
Email: [your email]

Call to action line:

“For more information or to schedule a private showing, contact Delia Moncrief.”

Include my business card details (office location etc.) in this section.

BROKERAGE + LOGOS

Use TKP QNV Realty logos provided

Place cleanly (bottom or footer)

Do not distort or restyle logos

FOOTER

Standard disclaimer if needed

Keep minimal

IMPORTANT NOTES

This is a SALE listing — do not use the word lease anywhere

Do not overdesign — clean always wins

Keep everything aligned and balanced

Make sure spacing feels high-end, not cramped
Updates

Please include this video link within the document: https://vidloom.example/tour/Kp7Qz2xLm9?ref=aB3cD4eF5gH6

State: Step inside. Watch the full video tour. and hyperlink Watch with the link

Target Market(s)

Buyers, Professionals, Lawyer Office, Family Office, Small FInancial Offices

Industry/Entity Type

Commercial Real Estate

Font styles to use
Serif
Sans Serif

Requirements
Must have
• Clean, clear, layout and good imagery
Should not have
• Professional flow, follow my font guidlines and thebrochure i shared as a guide

```html
<!DOCTYPE html>
<html lang="en">
<head>
<meta charset="utf-8">
<title>Office Condo Brickell | For Sale</title>
<link href="https://fonts.googleapis.com/css2?family=DM+Serif+Display&family=Poppins:wght@400;500;600;700&display=swap" rel="stylesheet">
<style>
:root{
  --navy:#0d3b6e;
  --navy-deep:#0b3466;
  --gold:#b39467;
  --ink:#1f1f1f;
  --muted:#4a4a4a;
  --stone:#eeece8;
  --label:#e9e7e3;
  --white:#ffffff;
}
*{margin:0;padding:0;box-sizing:border-box}
html,body{width:927px;height:1200px;overflow:hidden;background:var(--white)}
.page{position:relative;width:927px;height:1200px;font-family:"Poppins",sans-serif;color:var(--ink)}
.abs{position:absolute}

.headline{left:54px;top:44px;font-family:"DM Serif Display",serif;color:var(--navy);font-size:60px;line-height:61px;letter-spacing:-0.5px;font-weight:400}
.headline .bar{display:inline-block;width:1.5px;height:40px;background:var(--navy);vertical-align:-2px;margin:0 10px 0 8px}
.subhead{left:55px;top:182px;font-size:22px;color:var(--muted)}
.positioning{left:55px;top:218px;font-size:17px;color:var(--muted)}
.positioning .sep{margin:0 10px}

.section-title{font-family:"DM Serif Display",serif;font-size:29px;color:var(--ink);letter-spacing:-0.4px;font-weight:400;white-space:nowrap}
.rule{height:1.5px;background:var(--ink)}

.bullets{list-style:none;font-size:15px;color:var(--ink)}
.bullets li{position:absolute;white-space:nowrap}
.bullets li::before{content:"";position:absolute;left:-17px;top:9px;width:4px;height:4px;border-radius:50%;background:var(--ink)}
.bullets li.first::before{background:var(--gold)}

.hero{left:573px;top:0;width:354px;height:544px;background:linear-gradient(170deg,#4f9ae6 0%,#2f6fb4 35%,#3c6f9c 62%,#5f8a74 88%,#3e5a3e 100%)}

.price-card{left:605px;top:377px;width:290px;height:167px;background:var(--white)}
.price-label{left:29px;top:23px;width:232px;height:37px;background:var(--label);color:var(--gold);font-size:16px;letter-spacing:4.5px;text-align:center;line-height:37px}
.price{left:0;top:62px;width:290px;text-align:center;font-family:"DM Serif Display",serif;color:var(--navy);font-size:42px}
.psf{left:0;top:115px;width:290px;text-align:center;font-size:16px;letter-spacing:3.5px;color:var(--muted)}
.price-rule{left:49px;bottom:0;width:192px;height:2px;background:var(--gold)}

.location{left:605px;top:544px;width:290px;height:167px;background:var(--stone);text-align:center}
.location .label{margin-top:27px;color:var(--gold);font-size:16px;letter-spacing:4.5px}
.location address{font-style:normal;margin-top:12px;font-size:16px;line-height:23.5px;color:var(--ink)}
.location strong{font-weight:700}

.gallery .photo{top:721px;height:149px}
.ph-office{left:0;width:225px;background:linear-gradient(160deg,#f2ede4,#d8d2c7 55%,#4d4d55)}
.ph-open{left:234px;width:225px;background:linear-gradient(180deg,#f4f2ee,#e2ded6 55%,#5a5a60)}
.ph-kitchen{left:468px;width:224px;background:linear-gradient(160deg,#c9ced3,#e6e1d8 50%,#b3a893)}
.ph-conference{left:702px;width:225px;background:linear-gradient(170deg,#efe6da,#e4cfb4 55%,#4c4c52)}

.tour{left:32px;top:889px;width:863px;height:30px;display:flex;align-items:center}
.tour .line{height:1.5px;background:var(--navy);flex:none}
.tour .line-left{width:105px;margin-right:19px}
.tour .line-right{flex:1;margin-left:18px}
.tour-text{font-size:18px;font-weight:700;letter-spacing:4.9px;color:var(--navy);white-space:nowrap;line-height:30px;margin-right:11px}
.tour-text a{color:var(--navy);text-decoration:none}
.tour-icon{flex:none}

.contact{left:0;top:935px;width:927px;height:221px;background:var(--stone)}
.agent-photo{left:32px;top:19px;width:122px;height:184px;background:linear-gradient(180deg,#d8d5cf,#cfcbc4 50%,#e9e7e3)}
.agent-name{left:175px;top:18px;font-family:"DM Serif Display",serif;font-size:33px;color:var(--muted);letter-spacing:-0.3px;font-weight:400}
.agent-title{left:175px;top:64px;font-size:18px;letter-spacing:5.5px;color:var(--gold)}
.agent-title sup{font-size:10px;letter-spacing:0}
.agent-phone{left:175px;top:88px;font-size:24px;color:var(--ink)}
.contact-line{font-size:15.5px;color:var(--ink);display:flex;align-items:center}
.contact-email{left:175px;top:133px}
.contact-office{left:457px;top:129px;line-height:18px}
.contact-line svg{margin-right:12px;flex:none}
.cta{left:175px;top:178px;font-size:15px;font-weight:700;color:var(--navy)}

.brokerage{left:605px;top:12px;width:290px;height:87px;background:var(--white);display:flex;align-items:center;justify-content:center;text-align:center}
.brokerage span{font-family:"Poppins",sans-serif;font-weight:600;color:var(--ink);font-size:15px;line-height:20px;letter-spacing:0.5px;text-transform:uppercase}

.footer{left:0;top:1156px;width:927px;height:44px;background:var(--navy-deep);border-top:2px solid var(--gold)}
.footer p{position:absolute;left:69px;top:10px;font-family:"DM Serif Display",serif;color:var(--white);font-size:15px}
</style>
</head>
<body>
<main class="page">

  <h1 class="abs headline">Office Condo<br>Brickell<span class="bar"></span>For Sale</h1>
  <p class="abs subhead">2,146 SF Move-In Ready Office Suite</p>
  <p class="abs positioning">Corner Unit<span class="sep">|</span>Central Business District</p>

  <h2 class="abs section-title" style="left:55px;top:278px">Property Overview</h2>
  <div class="abs rule" style="left:317px;top:301px;width:213px"></div>
  <ul class="bullets">
    <li class="first" style="left:74px;top:334px">2,146 SF Office Suite</li>
    <li style="left:74px;top:366px">4 Private Offices</li>
    <li style="left:74px;top:398px">Reception Area</li>
    <li style="left:74px;top:430px">Conference Room</li>
    <li style="left:313px;top:337px">Printer / Copy Room</li>
    <li style="left:313px;top:369px">Kitchenette</li>
    <li style="left:313px;top:401px">Corner Unit Location</li>
    <li style="left:313px;top:432px">Natural Light &amp; Open Outlook</li>
  </ul>

  <h2 class="abs section-title" style="left:57px;top:503px">Additional Details</h2>
  <div class="abs rule" style="left:296px;top:522px;width:235px"></div>
  <ul class="bullets">
    <li style="left:74px;top:558px">Building: 1450 Harborline Avenue</li>
    <li style="left:74px;top:594px">Parking: Covered + Guest Parking</li>
    <li style="left:74px;top:631px">Security: On-site Security Guard</li>
    <li style="left:374px;top:558px">Year Built: 1982</li>
    <li style="left:374px;top:594px">Zoning: 6407</li>
    <li style="left:374px;top:631px">HVAC: Central Building A/C</li>
  </ul>

  <div class="abs hero" role="img" aria-label="Glass office tower with reflective curtain wall against a blue sky, palm trees at street level"></div>

  <div class="abs price-card">
    <div class="abs price-label">FOR SALE</div>
    <div class="abs price">$1,025,000</div>
    <div class="abs psf">$477 / SF</div>
    <div class="abs price-rule"></div>
  </div>

  <section class="abs location">
    <p class="label">LOCATION</p>
    <address><strong>1450 Harborline Avenue,</strong><br>Suite 505-B<br>Miami, FL 33131</address>
  </section>

  <div class="gallery">
    <div class="abs photo ph-office" role="img" aria-label="Private office with desk, chairs and window view"></div>
    <div class="abs photo ph-open" role="img" aria-label="Open workspace with carpeted floor and ceiling lights"></div>
    <div class="abs photo ph-kitchen" role="img" aria-label="Kitchenette with stainless refrigerator, counter and stools"></div>
    <div class="abs photo ph-conference" role="img" aria-label="Conference room with oval wooden table and window"></div>
  </div>

  <div class="abs tour">
    <div class="line line-left"></div>
    <p class="tour-text">STEP INSIDE. <a href="https://vidloom.example/tour/Kp7Qz2xLm9?ref=aB3cD4eF5gH6">WATCH</a> THE FULL VIDEO TOUR.</p>
    <svg class="tour-icon" width="30" height="30" viewBox="0 0 30 30" aria-hidden="true">
      <circle cx="15" cy="15" r="13.5" fill="none" stroke="var(--gold)" stroke-width="1.6"/>
      <path d="M8.5 11.5h13L15 19z" fill="var(--gold)"/>
    </svg>
    <div class="line line-right"></div>
  </div>

  <section class="abs contact">
    <div class="abs agent-photo" role="img" aria-label="Portrait of the realtor in a white blazer"></div>
    <h3 class="abs agent-name">Delia Moncrief</h3>
    <p class="abs agent-title">REALTOR<sup>®</sup></p>
    <p class="abs agent-phone">305.555.0148</p>
    <p class="abs contact-line contact-email">
      <svg width="28" height="28" viewBox="0 0 28 28" aria-hidden="true">
        <circle cx="14" cy="14" r="12.5" fill="none" stroke="var(--gold)" stroke-width="1.3"/>
        <rect x="8" y="10" width="12" height="8.5" rx="1" fill="var(--gold)"/>
        <path d="M8.5 10.5l5.5 4.3 5.5-4.3" fill="none" stroke="var(--stone)" stroke-width="1"/>
      </svg>
      deliamoncrief@example.com
    </p>
    <p class="abs contact-line contact-office">
      <svg width="28" height="28" viewBox="0 0 28 28" aria-hidden="true">
        <circle cx="14" cy="14" r="12.5" fill="none" stroke="var(--gold)" stroke-width="1.3"/>
        <path d="M14 7.5a4.5 4.5 0 0 1 4.5 4.5c0 3.4-4.5 8.5-4.5 8.5s-4.5-5.1-4.5-8.5A4.5 4.5 0 0 1 14 7.5z" fill="none" stroke="var(--gold)" stroke-width="1.3"/>
        <circle cx="14" cy="12" r="1.6" fill="var(--gold)"/>
      </svg>
      <span>418 Alcove Terrace<br>Coral Gables, FL 33146</span>
    </p>
    <p class="abs cta">For more information or to schedule a private showing, contact Delia Moncrief.</p>
    <div class="abs brokerage"><span>Tallowbrook Keystead<br>Partners QNV Realty</span></div>
  </section>

  <footer class="abs footer"><p>Information is believed to be accurate but not guaranteed.</p></footer>
</main>
</body>
</html>
```